International Film making Business needs the 5 Logos provided made into a POSTER Format

Design Task:
CREATE A POSTER DESIGN USING THE 5 LOGOS PROVIDED. The BOLD OPEN HORIZON LOGO should stand out from the others by being in the middle with the other 4 logos connected to it somehow.

The 5 Businesses already has their 5 Logos, all similar in design to each other.

BOLD OPEN HORIZON is the Main Logo that encompasses the other 4 Logos. So it must stand out more and it is like the Overall Business entity that incorporates the other 4 Logos.

What is required is that by using the 5 Logo designs provided, create a cool graphic artwork that somehow incorporates ALL of the 5 Logos - But having the BOLD OPEN HORIZON Logo at the forefront/most important/standing out the most.
- BOLD OPEN HORIZON will probably be bigger than the others
- and could be changed into 3D.

I have attached all 5 logos and a hand drawn example of how the BOLD OPEN HORIZONS could stand out from the rest.

THE DESIGNS OF THE LOGOS SHOULD NOT BE CHANGED (except the BOLDOPENHORIZON which can be 3D)

Please do not be restricted with the sample idea. Creativity is encouraged

DIMENSION: 3000 mm x 6000 mm
high resolution graphic

Logo Text

bold open , bold open pictures, bold open stories, bold open groovy, BOLD OPEN HORIZONS

Requirements
Must have
• USE THE 5 LOGOS PROVIDED ONLY - Only BOLD OPEN HORIZON can be changed into 3D only
Nice to have
• Eye catching design, showing the Bold Open Horizon as the most powerful Logo that has the other 4 as subordinate companies
Should not have
• ANY CHANGE IN THE 5 LOGO DESIGNS (EXcept 3D for Bold Open Horizons)

```html
<!DOCTYPE html>
<html lang="en">
<head>
<meta charset="utf-8">
<title>Bold Open Horizons – Poster</title>
<link href="https://fonts.googleapis.com/css2?family=Noto+Serif:wght@400;700&family=Montserrat:wght@500;600&display=swap" rel="stylesheet">
<style>
  :root {
    --page: #c9c9c9;
    --navy-top: #1d3361;
    --navy-mid: #0f1a30;
    --stage-black: #030305;
    --footer: #050c1f;
    --white: #ffffff;
    --serif: "Noto Serif", Georgia, serif;
    --sans: "Montserrat", Arial, sans-serif;
  }
  * { margin: 0; padding: 0; box-sizing: border-box; }
  html, body { width: 1200px; height: 1200px; overflow: hidden; }
  body {
    background: var(--page);
    display: flex; align-items: center; justify-content: center;
  }
  .poster {
    position: relative;
    width: 1200px; height: 600px;
    overflow: hidden;
    background: radial-gradient(ellipse 70% 60% at 50% 0%, #2a3f66 0%, transparent 70%),
                linear-gradient(180deg, var(--navy-top) 0%, var(--navy-mid) 45%, var(--stage-black) 80%);
  }
  .stage { position: absolute; inset: 0; width: 1200px; height: 600px; }
  .headline {
    position: absolute; top: 22px; left: 0; right: 0;
    text-align: center; color: var(--white);
    font-family: var(--serif); line-height: 1.08;
  }
  .headline__lead { font-weight: 400; font-size: 44px; display: block; }
  .headline__main { font-weight: 700; font-size: 42px; display: block; }
  .contact-bar {
    position: absolute; left: 0; right: 0; bottom: 0; height: 55px;
    background: var(--footer);
    display: flex; align-items: center; justify-content: center; gap: 44px;
    color: var(--white); font-family: var(--sans); font-weight: 600;
    font-size: 14px; letter-spacing: 2.4px;
  }
  .contact-bar__item { display: flex; align-items: center; gap: 14px; }
  .contact-bar__divider { width: 2px; height: 22px; background: var(--white); }
  .contact-bar svg { width: 20px; height: 20px; fill: none; stroke: var(--white); stroke-width: 1.6; }
</style>
</head>
<body>
<main class="poster">
  <svg class="stage" viewBox="0 0 1695 848" preserveAspectRatio="none">
    <defs>
      <linearGradient id="beam" x1="0" y1="0" x2="0" y2="1">
        <stop offset="0" stop-color="#ffffff" stop-opacity="0"/>
        <stop offset="0.6" stop-color="#ffffff" stop-opacity="0.75"/>
        <stop offset="1" stop-color="#ffffff" stop-opacity="1"/>
      </linearGradient>
      <radialGradient id="spot" cx="0.5" cy="0.5" r="0.5">
        <stop offset="0" stop-color="#ffffff" stop-opacity="0.95"/>
        <stop offset="0.15" stop-color="#b8ccf0" stop-opacity="0.6"/>
        <stop offset="1" stop-color="#6c86b8" stop-opacity="0"/>
      </radialGradient>
      <linearGradient id="ray" x1="0" y1="0" x2="1" y2="0">
        <stop offset="0" stop-color="#dfe8ff" stop-opacity="0.55"/>
        <stop offset="1" stop-color="#dfe8ff" stop-opacity="0"/>
      </linearGradient>
      <radialGradient id="topFace" cx="0.5" cy="0.5" r="0.5">
        <stop offset="0.6" stop-color="#ffffff"/>
        <stop offset="1" stop-color="#e4e4e4"/>
      </radialGradient>
      <linearGradient id="goldBody" x1="0" y1="0" x2="1" y2="0">
        <stop offset="0" stop-color="#4a3208"/><stop offset="0.3" stop-color="#c98f25"/>
        <stop offset="0.55" stop-color="#ffc53f"/><stop offset="0.8" stop-color="#b07a1c"/>
        <stop offset="1" stop-color="#2e1f05"/>
      </linearGradient>
      <linearGradient id="blueBody" x1="0" y1="0" x2="1" y2="0">
        <stop offset="0" stop-color="#1a6fc0"/><stop offset="0.5" stop-color="#15a4e6"/><stop offset="1" stop-color="#0b5ca8"/>
      </linearGradient>
      <linearGradient id="greenBody" x1="0" y1="0" x2="1" y2="0">
        <stop offset="0" stop-color="#0c5a0a"/><stop offset="0.5" stop-color="#2fd016"/><stop offset="1" stop-color="#0c4f08"/>
      </linearGradient>
      <linearGradient id="silverBody" x1="0" y1="0" x2="1" y2="0">
        <stop offset="0" stop-color="#3d3d3d"/><stop offset="0.5" stop-color="#d2d2d2"/><stop offset="1" stop-color="#3a3a3a"/>
      </linearGradient>
      <linearGradient id="magentaBody" x1="0" y1="0" x2="1" y2="0">
        <stop offset="0" stop-color="#4e0a55"/><stop offset="0.55" stop-color="#e20ce4"/><stop offset="1" stop-color="#520756"/>
      </linearGradient>
      <linearGradient id="filmsLink" x1="0" y1="0" x2="1" y2="0">
        <stop offset="0" stop-color="#cfcfcf"/><stop offset="1" stop-color="#f5b81c"/>
      </linearGradient>
      <linearGradient id="storiesLink" x1="0" y1="0" x2="1" y2="0">
        <stop offset="0" stop-color="#f5b81c"/><stop offset="1" stop-color="#d61a8a"/>
      </linearGradient>
    </defs>

    <g class="stage-lights">
      <polygon points="330,5 1000,360 700,520" fill="url(#ray)" opacity="0.45"/>
      <polygon points="1370,5 700,360 1000,520" fill="url(#ray)" opacity="0.45"/>
      <polygon points="35,150 600,420 420,520" fill="url(#ray)" opacity="0.35"/>
      <polygon points="1670,140 1100,420 1280,520" fill="url(#ray)" opacity="0.35"/>
      <polygon points="20,440 420,320 420,420" fill="url(#ray)" opacity="0.3"/>
      <polygon points="1680,440 1280,320 1280,420" fill="url(#ray)" opacity="0.3"/>
      <ellipse cx="330" cy="5" rx="110" ry="70" fill="url(#spot)"/>
      <ellipse cx="1370" cy="5" rx="110" ry="70" fill="url(#spot)"/>
      <ellipse cx="35" cy="150" rx="90" ry="40" fill="url(#spot)"/>
      <ellipse cx="1670" cy="142" rx="110" ry="50" fill="url(#spot)"/>
      <ellipse cx="22" cy="442" rx="60" ry="30" fill="url(#spot)" opacity="0.6"/>
      <ellipse cx="1678" cy="444" rx="60" ry="30" fill="url(#spot)" opacity="0.6"/>
    </g>

    <g class="connectors" fill="none" stroke-width="3" stroke-dasharray="1 6" stroke-linecap="round">
      <path d="M469,488 V623 H644" stroke="#f5b81c"/>
      <path d="M1230,493 V621 H1022" stroke="#f5b81c"/>
      <path d="M206,708 V746 H617 L735,698" stroke="url(#filmsLink)"/>
      <path d="M1516,716 V748 H1072 L929,698" stroke="url(#storiesLink)"/>
    </g>
    <ellipse class="hub-ring" cx="834" cy="646" rx="192" ry="62" fill="none" stroke="#b78520" stroke-width="4"/>
    <g class="hub-nodes" fill="#f5b81c" stroke="#6b4a10" stroke-width="2">
      <ellipse cx="645" cy="622" rx="8" ry="5"/><ellipse cx="1022" cy="621" rx="8" ry="5"/>
      <ellipse cx="736" cy="698" rx="8" ry="5"/><ellipse cx="929" cy="698" rx="8" ry="5"/>
    </g>

    <g class="beams">
      <rect x="108" y="408" width="182" height="210" fill="url(#beam)"/>
      <rect x="375" y="188" width="183" height="210" fill="url(#beam)"/>
      <rect x="682" y="218" width="304" height="315" fill="url(#beam)"/>
      <rect x="1124" y="198" width="182" height="200" fill="url(#beam)"/>
      <rect x="1413" y="438" width="182" height="190" fill="url(#beam)"/>
    </g>

    <g class="pedestal pedestal--pictures">
      <path d="M107,618 V675 A93,30 0 0 0 293,675 V618 Z" fill="url(#silverBody)"/>
      <ellipse cx="200" cy="618" rx="93" ry="30" fill="url(#topFace)" stroke="#8a8a8a" stroke-width="3"/>
    </g>
    <g class="pedestal pedestal--bold-open">
      <path d="M374,398 V452 A93,30 0 0 0 560,452 V398 Z" fill="url(#blueBody)"/>
      <ellipse cx="467" cy="398" rx="93" ry="30" fill="url(#topFace)" stroke="#1583d0" stroke-width="3"/>
    </g>
    <g class="pedestal pedestal--horizons">
      <path d="M679,533 V623 A155,55 0 0 0 989,623 V533 Z" fill="url(#goldBody)"/>
      <ellipse cx="834" cy="533" rx="155" ry="55" fill="url(#topFace)" stroke="#c08a22" stroke-width="3"/>
    </g>
    <g class="pedestal pedestal--groovy">
      <path d="M1121,398 V452 A93,30 0 0 0 1307,452 V398 Z" fill="url(#greenBody)"/>
      <ellipse cx="1214" cy="398" rx="93" ry="30" fill="url(#topFace)" stroke="#2bc51a" stroke-width="3"/>
    </g>
    <g class="pedestal pedestal--stories">
      <path d="M1411,628 V680 A93,30 0 0 0 1597,680 V628 Z" fill="url(#magentaBody)"/>
      <ellipse cx="1504" cy="628" rx="93" ry="30" fill="url(#topFace)" stroke="#d414d6" stroke-width="3"/>
    </g>

    <g class="brand-names" font-family="Noto Serif, Georgia, serif" font-weight="400" text-anchor="middle">
      <g class="brand brand--pictures" fill="#7b7b7b" font-size="20">
        <circle cx="138" cy="556" r="12"/>
        <text x="218" y="550">BOLD OPEN</text>
        <text x="218" y="574">PICTURES</text>
      </g>
      <g class="brand brand--bold-open" fill="#1e7fc8" font-size="24">
        <circle cx="394" cy="330" r="13"/>
        <text x="490" y="322">BOLD OPEN</text>
        <text x="490" y="351">HORIZON</text>
      </g>
      <g class="brand brand--horizons" fill="#b8872a" font-size="30">
        <circle cx="733" cy="435" r="22"/>
        <text x="862" y="420">BOLD OPEN</text>
        <text x="862" y="453">HORIZONS</text>
        <text x="862" y="470" font-size="11" letter-spacing="1.5">boldopenhorizons.com.au</text>
      </g>
      <g class="brand brand--groovy" fill="#1f9e1a" font-size="22">
        <circle cx="1214" cy="286" r="14"/>
        <text x="1214" y="330">BOLD OPEN</text>
        <text x="1214" y="357">GROOVY</text>
      </g>
      <g class="brand brand--stories" fill="#c21ac4" font-size="20">
        <circle cx="1444" cy="572" r="12"/>
        <text x="1526" y="564">BOLD OPEN</text>
        <text x="1526" y="588">STORIES</text>
      </g>
    </g>
  </svg>

  <h1 class="headline">
    <span class="headline__lead">Lorem Ipsum</span>
    <span class="headline__main">is simply dummy text</span>
  </h1>

  <footer class="contact-bar">
    <span class="contact-bar__item">
      <svg viewBox="0 0 24 24"><path d="M3 9 C3 5 21 5 21 9 V10 H16 V8 H8 V10 H3 Z M6 11 H18 L20 20 H4 Z" fill="#fff" stroke="none"/></svg>
      123 456 789
    </span>
    <span class="contact-bar__divider"></span>
    <span class="contact-bar__item">
      <svg viewBox="0 0 24 24"><rect x="2" y="5" width="20" height="14"/><path d="M2 5 L12 13 L22 5 M2 19 L9 11 M22 19 L15 11"/></svg>
      info@boldopenhorizons.com
    </span>
    <span class="contact-bar__divider"></span>
    <span class="contact-bar__item">
      <svg viewBox="0 0 24 24"><circle cx="12" cy="12" r="10"/><ellipse cx="12" cy="12" rx="4.5" ry="10"/><path d="M2 12 H22 M4 7 H20 M4 17 H20"/></svg>
      boldopenhorizons.com.au
    </span>
  </footer>
</main>
</body>
</html>
```